Helicopter company requires newspaper ad

"Ridgeline Aviation" is an agricultural helicopter company based in Victoria, Australia. We need an advert design for use in newspapers and also possibly social media. Our company specialises in using a helicopter for various agricultural work such as Spraying weeds ("Cropdusting"), spreading fertiliser. This advert will be targeted at farmers in our service area, Our customers are mainly dairy and cow farmers and our services are aimed at increasing their farm productivity. The final design should inform potential and existing customers about our services and the benefits of them. I will attach files of our logo and some existing advertising material for guidance. We would like the ad to feature the blue and green colours in our logo Please feel free to view our website and facebook page to see more about what we do. www.ridgelineaviation.com.au Some text we would like included Spraying: -Accurate -Time Efficient -Zero crop damage -Cost efficient Fertiliser Spreading: -Accurate, Pattern-tested equipment -Zero crop damage or wheel marks -Ability to load product out of a truck, bin or bulk bags -Cost effective, Prices from $32 per hectare depending on spread rate The final advert size should be 195 mm wide x 186 mm high Thanks :)

Farmers, Agriculture Industry

Agribusiness

Designer to choose colors to be used in the design.

• Phone number 0491 736 058
• The text included in the decription, or variations of this

```html
<!DOCTYPE html>
<html lang="en">
<head>
<meta charset="utf-8">
<title>Ridgeline Aviation – Summer Spraying &amp; Spreading</title>
<link rel="stylesheet" href="https://fonts.googleapis.com/css2?family=Kaushan+Script&family=Montserrat:wght@400;500;600;700&family=Open+Sans:wght@700;800&display=swap">
<style>
  :root {
    --ink: #111111;
    --paper: #ffffff;
    --band-light: #f4f4f4;
    --band-grey: #dcdcdc;
    --footer-cyan: #0cc0d4;
    --footer-blue: #2f8fd8;
    --footer-violet: #4d6ce0;
    --accent-yellow: #fbdc4a;
    --brand-blue: #2f74c0;
    --sky-pale: #8db0d2;
    --sky-deep: #3f7fd8;
    --field-green: #4f7a34;
    --field-light: #7aa650;
  }
  * { margin: 0; padding: 0; box-sizing: border-box; }
  html, body { width: 1200px; height: 1145px; overflow: hidden; background: var(--paper); }
  .ad { position: relative; width: 1200px; height: 1145px; background: var(--paper); font-family: "Montserrat", sans-serif; color: var(--ink); }

  .headline-band {
    position: absolute; left: 0; top: 0; width: 1200px; height: 125px;
    background: linear-gradient(90deg, var(--band-grey), var(--band-light));
    clip-path: polygon(0 0,100% 0,100% 88%,86% 92%,70% 88%,52% 93%,34% 89%,18% 92%,0 88%);
  }
  .headline {
    position: absolute; left: 0; top: 24px; width: 1200px; text-align: center;
    white-space: nowrap;
    font-family: "Kaushan Script", cursive; font-weight: 400; font-size: 58px; line-height: 1.1; color: var(--ink);
  }

  .photo { position: absolute; }
  .photo--spraying {
    left: 38px; top: 183px; width: 470px; height: 310px;
    background: linear-gradient(180deg, var(--sky-pale) 0%, #b7cbe0 55%, var(--field-light) 72%, var(--field-green) 100%);
    clip-path: polygon(0 2.5%,30% 0,100% 0,100% 100%,2% 100%);
  }
  .photo--spreading {
    left: 46px; top: 529px; width: 466px; height: 313px;
    background: linear-gradient(180deg, var(--sky-deep) 0%, #7fb7f0 58%, var(--field-light) 68%, var(--field-green) 100%);
    clip-path: polygon(0 0,50% 0,99% 2%,100% 100%,0.5% 100%);
  }

  .service-title {
    position: absolute; font-family: "Montserrat", sans-serif; font-weight: 500;
    font-size: 56px; line-height: 1; white-space: nowrap;
    color: var(--paper);
    text-shadow:
      2px 0 0 var(--ink), -2px 0 0 var(--ink), 0 2px 0 var(--ink), 0 -2px 0 var(--ink),
      1.5px 1.5px 0 var(--ink), -1.5px 1.5px 0 var(--ink), 1.5px -1.5px 0 var(--ink), -1.5px -1.5px 0 var(--ink);
  }
  .service-title--spraying { left: 602px; top: 184px; letter-spacing: 0.24em; }
  .service-title--spreading { left: 582px; top: 544px; letter-spacing: 0.2em; }

  .benefits { position: absolute; list-style: none; font-size: 25px; line-height: 42.7px; }
  .benefits li { position: relative; padding-left: 28px; }
  .benefits li::before {
    content: ""; position: absolute; left: 0; top: 19px; width: 7px; height: 7px;
    border-radius: 50%; background: var(--ink);
  }
  .benefits--spraying { left: 607px; top: 273px; }
  .benefits--spreading { left: 585px; top: 617px; width: 575px; }

  .footer {
    position: absolute; left: 0; top: 906px; width: 1200px; height: 239px;
    background: linear-gradient(90deg, var(--footer-cyan), var(--footer-blue) 55%, var(--footer-violet));
  }
  .laptop { position: absolute; left: 38px; top: 28px; width: 334px; height: 194px; }
  .laptop-name {
    position: absolute; left: 68px; top: 73px; width: 274px; text-align: center;
    font-family: "Open Sans", sans-serif; font-weight: 800; font-size: 30px; line-height: 1.15;
    color: var(--brand-blue);
  }
  .tagline {
    position: absolute; left: 420px; top: 24px; white-space: nowrap;
    font-family: "Open Sans", sans-serif; font-weight: 800; font-size: 50px; line-height: 1;
    color: var(--accent-yellow);
  }
  .specialism {
    position: absolute; left: 421px; top: 92px; white-space: nowrap;
    font-family: "Montserrat", sans-serif; font-weight: 700; font-size: 25px; letter-spacing: 0.26em;
    color: var(--paper);
  }
  .contact {
    position: absolute; top: 171px; display: flex; align-items: center; gap: 10px; white-space: nowrap;
    font-family: "Open Sans", sans-serif; font-weight: 700; color: var(--paper);
  }
  .contact--phone { left: 427px; font-size: 27px; }
  .contact--web { left: 787px; font-size: 24px; gap: 16px; }
  .contact svg { flex: none; }
</style>
</head>
<body>
<main class="ad">
  <header>
    <div class="headline-band"></div>
    <h1 class="headline">Summer Crops need Spraying or Fertilizer ?</h1>
  </header>

  <section class="service">
    <div class="photo photo--spraying" role="img" aria-label="Helicopter with spray boom misting a green paddock under a blue sky"></div>
    <h2 class="service-title service-title--spraying">SPRAYING</h2>
    <ul class="benefits benefits--spraying">
      <li>Accurate</li>
      <li>Time Efficient</li>
      <li>Zero Crop Damage</li>
      <li>Cost Effective</li>
    </ul>
  </section>

  <section class="service">
    <div class="photo photo--spreading" role="img" aria-label="Helicopter carrying a spreader bucket releasing fertiliser over rolling green hills with trees"></div>
    <h2 class="service-title service-title--spreading">SPREADING</h2>
    <ul class="benefits benefits--spreading">
      <li>Accurate, Pattern-tested equipment</li>
      <li>Zero crop damage or wheel marks</li>
      <li>Ability to load out of a Truck, Bin or bulk-bags</li>
      <li>Competitive Prices (from $32 per hectare depending on spread rate)</li>
    </ul>
  </section>

  <footer class="footer">
    <svg class="laptop" viewBox="0 0 334 194" aria-hidden="true">
      <rect x="30" y="0" width="274" height="184" rx="8" fill="#111"/>
      <rect x="40" y="10" width="254" height="164" fill="#fff"/>
      <rect x="0" y="182" width="334" height="10" rx="4" fill="#d9dde2"/>
      <rect x="142" y="182" width="50" height="4" rx="2" fill="#b9bec5"/>
    </svg>
    <div class="laptop-name">Ridgeline<br>Aviation</div>

    <p class="tagline">owner/operated</p>
    <p class="specialism">AERIAL AGRICULTURE SPECIALIST</p>

    <p class="contact contact--phone">
      <svg width="40" height="40" viewBox="0 0 40 40" aria-hidden="true">
        <path d="M9 8c2-2 4-2 5 0l3 5c1 2 0 3-1 4l-2 2c1 4 5 8 9 9l2-2c1-1 2-2 4-1l5 3c2 1 2 3 0 5l-3 3c-3 2-10 0-17-7S6 11 9 8z" fill="#fff" stroke="#111" stroke-width="1.5"/>
        <path d="M24 4a12 12 0 0 1 12 12M24 9a7 7 0 0 1 7 7" fill="none" stroke="#fff" stroke-width="2.5" stroke-linecap="round"/>
      </svg>
      0491 736 058
    </p>
    <p class="contact contact--web">
      <svg width="43" height="43" viewBox="0 0 44 44" aria-hidden="true">
        <circle cx="22" cy="22" r="20" fill="none" stroke="#fff" stroke-width="2.5"/>
        <ellipse cx="22" cy="22" rx="9" ry="20" fill="none" stroke="#fff" stroke-width="2"/>
        <path d="M4 14h36M4 30h36" stroke="#fff" stroke-width="2"/>
        <rect x="6" y="17" width="32" height="10" rx="2" fill="#2f8fd8" stroke="#fff" stroke-width="1.5"/>
        <text x="22" y="25" text-anchor="middle" font-family="Open Sans, sans-serif" font-size="8" font-weight="700" fill="#fff">www</text>
      </svg>
      ridgelineaviation.com.au
    </p>
  </footer>
</main>
</body>
</html>
```